Professional business cards for real estate development company

I need business cards for my new real estate development company. The company, "KORVA" is a real estate development, investment, and advisory firm with a focus on multifamily, office, and mixed-use projects across primary and secondary markets in the Southeast United States.

Style preference is modern

Industry/Entity Type

Real Estate Development

Contact Information for Business Card

The business cards need to include:
Name
Title
Mailing Address
Phone Number
Web Address

Logo is attached. I would like white to be the primary color with incorporation of the company colors: #232D3A and #B5A451

Font styles to use
Other font styles liked:
• Montserrat, Avenir

Requirements
Must have
• Company Logo. No need to include the company name since the name is in the logo.
Should not have
• No line type designs

```html
<!DOCTYPE html>
<html lang="en">
<head>
<meta charset="utf-8">
<title>KORVA Business Card</title>
<link rel="stylesheet" href="https://fonts.googleapis.com/css2?family=Roboto:wght@400;500&display=swap">
<style>
  :root {
    --stage: #3a3b3e;
    --navy: #232D3A;
    --gold: #B5A451;
    --paper: #ffffff;
    --ink: #232D3A;
    --ink-soft: #4a5361;
    --mark-light: #ffffff;
  }
  * { margin: 0; padding: 0; box-sizing: border-box; }
  html, body { width: 799px; height: 1200px; overflow: hidden; }
  body {
    background: var(--stage);
    font-family: "Roboto", Arial, sans-serif;
    position: relative;
  }
  .card {
    position: absolute;
    left: 100px;
    width: 600px;
    height: 343px;
    border-radius: 3px;
    overflow: hidden;
    box-shadow: 0 14px 30px rgba(0,0,0,.45);
  }
  .card-front { top: 130px; background: var(--navy); }
  .card-back { top: 730px; background: var(--paper); }

  .wordmark {
    position: absolute;
    display: flex;
    align-items: center;
    gap: 14px;
    font-weight: 500;
    letter-spacing: 4px;
    line-height: 1;
    color: var(--mark-light);
  }
  .wordmark-square {
    width: 44px;
    height: 44px;
    background: var(--gold);
  }
  .card-front .wordmark {
    left: 50%;
    top: 50%;
    transform: translate(-50%, -50%);
    font-size: 60px;
  }
  .card-back .curve { position: absolute; inset: 0; }
  .card-back .wordmark {
    left: 34px;
    top: 136px;
    font-size: 44px;
    gap: 12px;
  }
  .card-back .wordmark-square { width: 32px; height: 32px; }

  .person {
    position: absolute;
    right: 36px;
    top: 52px;
    text-align: right;
    color: var(--ink);
  }
  .person-name { font-size: 28px; font-weight: 500; }
  .person-title { font-size: 15px; color: var(--ink-soft); margin-top: 3px; }

  .contact {
    position: absolute;
    right: 30px;
    top: 170px;
    color: var(--ink);
    font-size: 17px;
    text-align: right;
  }
  .contact-address { margin-right: 27px; line-height: 1.3; margin-bottom: 16px; }
  .contact-row { display: flex; justify-content: flex-end; align-items: center; gap: 12px; line-height: 1.35; }
  .contact-row svg { width: 15px; height: 15px; fill: var(--gold); flex: none; }
</style>
</head>
<body>
  <section class="card card-front">
    <div class="wordmark"><span class="wordmark-square"></span>KORVA</div>
  </section>

  <section class="card card-back">
    <svg class="curve" viewBox="0 0 600 343" width="600" height="343" aria-hidden="true">
      <path d="M0 0 H250 A300 300 0 0 1 175 343 H0 Z" fill="var(--navy)"/>
    </svg>
    <div class="wordmark"><span class="wordmark-square"></span>KORVA</div>

    <div class="person">
      <div class="person-name">Daniel Reyes</div>
      <div class="person-title">Managing Director</div>
    </div>

    <div class="contact">
      <div class="contact-address">118 Harbor Lane, Suite 4,<br>Raleigh, NC 27601</div>
      <div class="contact-row">919-555-0142
        <svg viewBox="0 0 16 16"><path d="M3 2h3l1 3-2 1c1 2 2 3 4 4l1-2 3 1v3c0 1-1 2-2 2C6 14 2 10 2 4c0-1 0-2 1-2z"/></svg>
      </div>
      <div class="contact-row">daniel@korvadev.com
        <svg viewBox="0 0 16 16"><path d="M1 3h14v10H1z M1 3l7 6 7-6" fill="none" stroke="var(--gold)" stroke-width="1.6"/></svg>
      </div>
      <div class="contact-row">www.korvadev.com
        <svg viewBox="0 0 16 16"><circle cx="8" cy="8" r="7"/><path d="M1 8h14M8 1c-3 3-3 11 0 14M8 1c3 3 3 11 0 14" stroke="var(--paper)" stroke-width="1" fill="none"/></svg>
      </div>
    </div>
  </section>
</body>
</html>
```